Neon Lodging Offers Website looking for new design

We are a online travel discounter based around hotel accommodations in Las Vegas. We need a wordpress design that will be used as our corporate cover page, and also for the affiliate pages. The current design can be viewed at http://postweaveforum.com/clients/neonoffer/ and the final design needs to include most of the navigation components. The affiliate pages will need a space to display the booking engine, for example, as shown at http://www.qrv.travel/marcoti. Our general color scheme is red/black, and the two logos we use are attached.

Because this is a crowded niche it is extremely important that we set ourselves apart in the design. The more visually stunning and out of the box the design, the better. The site needs to look distinctively different than anything else online. Since the overall layout is very basic and does not have to provide a lot of information, it leaves a lot of flexibility in design concepts.

We realize it is a truncated timetable, which is why the increased fee for your time and guaranteed payout.

Industry/Entity Type

Travel

```html
<!DOCTYPE html>
<html lang="en">
<head>
<meta charset="utf-8">
<title>NeonLodging.Offers</title>
<link href="https://fonts.googleapis.com/css2?family=Oswald:wght@400;500&family=Roboto:wght@300;400;500&family=Open+Sans:wght@400;600&display=swap" rel="stylesheet">
<style>
:root{
  --red:#d0111b;
  --red-dark:#b50d16;
  --ink:#222;
  --text:#444;
  --line:#e3e3e3;
  --pale:#f6f6f6;
  --white:#fff;
  --navy:#1f5fa8;
}
*{margin:0;padding:0;box-sizing:border-box}
html,body{width:718px;height:1200px;overflow:hidden;background:var(--white)}
body{position:relative;font-family:"Roboto",Arial,sans-serif;color:var(--text)}
.abs{position:absolute}
.topline{left:0;top:0;width:718px;height:2px;background:#e9888c}

/* header */
.brand{left:58px;top:24px;display:flex;align-items:center;gap:8px;font:500 12px "Roboto",sans-serif;color:var(--red)}
.brand-mark{width:34px;height:34px;border-radius:50%;background:var(--red)}
.nav{left:258px;top:33px;display:flex;font:400 8.8px "Roboto",sans-serif;color:#333;letter-spacing:.3px}
.nav span{padding:0 12px;border-right:1px solid #e6e6e6;line-height:18px}
.nav span:last-child{border-right:0}
.search{left:546px;top:30px;width:112px;height:21px;background:#f3f3f3;border:1px solid #eee;font:400 7px "Open Sans",sans-serif;color:#666;padding:6px 8px}
.search svg{position:absolute;right:7px;top:5px}

/* hero */
.hero{left:0;top:78px;width:718px;height:382px;background:
  radial-gradient(ellipse 60px 18px at 230px 265px,rgba(255,235,190,.35),transparent),
  radial-gradient(ellipse 70px 20px at 360px 300px,rgba(255,230,180,.3),transparent),
  radial-gradient(ellipse 260px 90px at 420px 240px,#3fb6c9 0%,rgba(43,140,160,.85) 40%,transparent 100%),
  radial-gradient(ellipse 200px 60px at 600px 80px,rgba(230,190,120,.55),transparent),
  radial-gradient(ellipse 220px 70px at 150px 60px,rgba(190,140,80,.5),transparent),
  linear-gradient(180deg,#5a4330 0%,#3e2e22 28%,#2d5560 52%,#25383a 72%,#2a211b 100%)}
.hero-title{left:69px;top:166px;font:400 32px/1 "Oswald",sans-serif;color:var(--white)}
.hero-name{left:69px;top:206px;font:500 44px/1 "Oswald",sans-serif;color:var(--white);letter-spacing:-.5px}
.hero-sub{left:70px;top:261px;width:200px;font:400 10px/15px "Oswald",sans-serif;color:var(--white)}
.hero-btn{left:70px;top:300px;width:106px;height:27px;background:var(--red);color:var(--white);font:400 11px/27px "Oswald",sans-serif;text-align:center}
.arrow{top:260px;width:21px;height:21px;border-radius:50%;background:rgba(0,0,0,.55)}
.arrow svg{position:absolute;left:6px;top:5px}

/* booking bar */
.booking{left:59px;top:382px;width:599px;height:78px;background:var(--red);border-top:3px solid var(--white)}
.b-label{top:399px;font:400 9px "Roboto",sans-serif;color:var(--white)}
.b-field{top:422px;height:23px;background:var(--white);font:400 7px/23px "Open Sans",sans-serif;color:#666;padding-left:8px}
.b-field svg{position:absolute;right:7px;top:7px}
.b-go{left:611px;top:422px;width:35px;height:23px;background:#1a1a1a}
.b-go svg{position:absolute;left:12px;top:6px}

/* welcome */
.welcome{left:0;top:460px;width:718px;height:196px;background:var(--pale);border-bottom:1px solid #ececec}
.w-title{left:238px;top:480px;font:400 16px "Roboto",sans-serif;color:var(--ink)}
.w-title b{font-weight:400;color:var(--red)}
.w-text{left:238px;top:504px;width:230px;font:400 6.8px/12.8px "Open Sans",sans-serif;color:#333}
.w-list{left:238px;top:591px;font:400 7.8px "Open Sans",sans-serif;color:#333;list-style:none}
.w-list li{height:18px;display:flex;align-items:center;gap:8px}
.w-list i{width:6px;height:6px;border-radius:50%;background:var(--navy);display:block}
.room-cap{left:484px;top:612px;width:174px;font:400 8.5px "Roboto",sans-serif;color:var(--white);text-align:center}

/* cards */
.card{top:681px;width:141px;height:201px;background:var(--pale)}
.card .img{height:100px}
.card h3{margin:12px 8px 0;font:300 10px "Roboto",sans-serif;color:#222}
.card p{margin:6px 8px 0;font:400 6.2px/10px "Open Sans",sans-serif;color:#444}
.card .meta{margin:5px 8px 0;display:flex;align-items:center;gap:8px;font:500 7.5px "Roboto",sans-serif;color:var(--red)}
.card .stars{color:#e8a318;font-size:7px;letter-spacing:-.5px}
.card .stars em{color:#bbb;font-style:normal}
.card .btn{position:absolute;left:0;bottom:0;width:141px;height:27px;background:var(--red);color:var(--white);font:400 9.5px/27px "Roboto",sans-serif;padding-left:11px}
.card .btn span{position:absolute;right:0;top:0;width:30px;height:27px;background:var(--red-dark);text-align:center;font-size:10px}

/* contact */
.person{left:59px;top:904px;width:141px;height:218px;background:
  radial-gradient(ellipse 50px 70px at 70px 60px,#e9e5e1,transparent),
  linear-gradient(180deg,#ffffff 0%,#f4f4f4 35%,#5a5a5e 55%,#3b3b3f 100%)}
.c-title{left:219px;top:923px;font:400 12px "Roboto",sans-serif;color:#222}
.c-lines{left:219px;top:945px;font:300 9.5px/16.5px "Roboto",sans-serif;color:#333}
.c-icon{width:31px;height:31px;border-radius:50%;background:var(--white);border:1px solid #e5e5e5;box-shadow:0 1px 2px rgba(0,0,0,.08)}
.c-icon svg{position:absolute;left:8px;top:8px}
.c-addr{left:257px;font:400 7.6px/15.5px "Open Sans",sans-serif;color:#444}
.social{top:1095px;width:17px;height:17px;border-radius:50%}

/* enquiry */
.enquiry{left:440px;top:904px;width:218px;height:218px;background:var(--pale);border:1px solid #eee}
.e-title{left:450px;top:914px;font:500 10.5px "Roboto",sans-serif;color:#222;letter-spacing:.3px}
.e-label{width:44px;left:440px;font:400 7px "Open Sans",sans-serif;color:#444;text-align:right}
.e-input{left:497px;width:149px;background:var(--white);border:1px solid #e6e6e6}
.e-send{left:456px;top:1094px;width:190px;height:28px;background:var(--white);border-radius:95px 95px 0 0/22px 22px 0 0;text-align:center;font:400 8.5px/40px "Roboto",sans-serif;color:var(--red)}

/* footer */
.footer{left:0;top:1142px;width:718px;height:58px;background:var(--red)}
.f-links{left:58px;top:1157px;font:400 8.5px "Roboto",sans-serif;color:var(--white)}
.f-copy{left:56px;top:1178px;font:400 7px "Roboto",sans-serif;color:var(--white)}
</style>
</head>
<body>
<div class="abs topline"></div>

<header>
  <div class="abs brand"><span class="brand-mark"></span>NeonLodging.Offers</div>
  <nav class="abs nav"><span>HOME</span><span>GROUPS</span><span>SEARCH EVENTS</span><span>CONTACT US</span></nav>
  <div class="abs search">Search
    <svg width="9" height="9" viewBox="0 0 10 10"><circle cx="4" cy="4" r="3" fill="none" stroke="#333" stroke-width="1.4"/><line x1="6.2" y1="6.2" x2="9" y2="9" stroke="#333" stroke-width="1.6"/></svg>
  </div>
</header>

<section>
  <div class="abs hero" role="img" aria-label="Night view of a resort hotel with lit pool, palm trees and umbrellas"></div>
  <div class="abs hero-title">Welcome to</div>
  <div class="abs hero-name">NEONLODGING</div>
  <div class="abs hero-sub">Get wholesale rates on hotel accommodations with NeonLodging.Offers</div>
  <div class="abs hero-btn">HOTEL BOOKING NOW</div>
  <div class="abs arrow" style="left:17px"><svg width="9" height="11" viewBox="0 0 9 11"><path d="M6.5 1 L2 5.5 L6.5 10" fill="none" stroke="#fff" stroke-width="1.8"/></svg></div>
  <div class="abs arrow" style="left:679px"><svg width="9" height="11" viewBox="0 0 9 11"><path d="M2.5 1 L7 5.5 L2.5 10" fill="none" stroke="#fff" stroke-width="1.8"/></svg></div>
</section>

<section>
  <div class="abs booking"></div>
  <div class="abs b-label" style="left:70px">LOCATION</div>
  <div class="abs b-label" style="left:202px">CHECK-IN</div>
  <div class="abs b-label" style="left:295px">CHECK-OUT</div>
  <div class="abs b-label" style="left:387px">ROOMS</div>
  <div class="abs b-label" style="left:529px">RESIDENT</div>
  <div class="abs b-field" style="left:70px;width:124px">Please type city name</div>
  <div class="abs b-field" style="left:202px;width:84px">13/02/2015<svg width="8" height="8" viewBox="0 0 8 8"><rect x="0.5" y="1.5" width="7" height="6" fill="none" stroke="#666"/><rect x="0.5" y="1.5" width="7" height="2" fill="#666"/></svg></div>
  <div class="abs b-field" style="left:295px;width:83px">13/02/2015<svg width="8" height="8" viewBox="0 0 8 8"><rect x="0.5" y="1.5" width="7" height="6" fill="none" stroke="#666"/><rect x="0.5" y="1.5" width="7" height="2" fill="#666"/></svg></div>
  <div class="abs b-field" style="left:387px;width:63px">Adults<svg width="6" height="9" viewBox="0 0 6 9"><path d="M0 3.5 L3 0.5 L6 3.5Z M0 5.5 L3 8.5 L6 5.5Z" fill="#555"/></svg></div>
  <div class="abs b-field" style="left:458px;width:64px">Children<svg width="6" height="9" viewBox="0 0 6 9"><path d="M0 3.5 L3 0.5 L6 3.5Z M0 5.5 L3 8.5 L6 5.5Z" fill="#555"/></svg></div>
  <div class="abs b-field" style="left:529px;width:73px;padding-left:13px">Country</div>
  <div class="abs b-go"><svg width="11" height="11" viewBox="0 0 10 10"><circle cx="4" cy="4" r="3" fill="none" stroke="#fff" stroke-width="1.5"/><line x1="6.2" y1="6.2" x2="9" y2="9" stroke="#fff" stroke-width="1.8"/></svg></div>
</section>

<section>
  <div class="abs welcome"></div>
  <div class="abs" style="left:59px;top:482px;width:159px;height:153px;border:1px solid #ddd;background:radial-gradient(ellipse 60px 50px at 90px 60px,rgba(180,90,70,.55),transparent),radial-gradient(ellipse 50px 40px at 40px 110px,rgba(120,150,170,.5),transparent),linear-gradient(135deg,#9a928c,#6b635e 55%,#8c8580)" role="img" aria-label="Las Vegas strip at dusk, softened as a backdrop"></div>
  <h2 class="abs w-title">Welcome To <b>NeonLodging</b>.Offers</h2>
  <p class="abs w-text">Lorem ipsum dolor sit amet, consectetur adipiscing elit, sed do eiusmod tempor incididunt ut labore et dolore magna aliqua. Ut enim ad minim veniam, quis nostrud exercitation ullamco laboris nisi ut aliquip ex ea commodo consequat. Duis aute irure dolor in reprehenderit in voluptate velit esse cillum fugiat nulla pariatur. Lorem ipsum dolor sit amet, consectetur adipiscing elit.</p>
  <ul class="abs w-list">
    <li><i></i>Lorem ipsum dolor</li>
    <li><i></i>Praesent vestibulum molestie lacus</li>
    <li><i></i>cLorem ipsum dolor sit amet</li>
  </ul>
  <div class="abs" style="left:484px;top:482px;width:174px;height:153px;background:radial-gradient(ellipse 90px 20px at 87px 8px,#f6e6c4,transparent),radial-gradient(ellipse 60px 25px at 60px 110px,rgba(235,220,200,.7),transparent),linear-gradient(180deg,#cdb690 0%,#5e3f2c 40%,#3b2920 78%,#2b221d 100%)" role="img" aria-label="Deluxe hotel room with bed and wardrobe"></div>
  <div class="abs room-cap">DELUXEROOM</div>
</section>

<section>
  <article class="abs card" style="left:59px"><div class="img" style="background:radial-gradient(ellipse 40px 30px at 60px 55px,rgba(240,190,120,.6),transparent),linear-gradient(160deg,#2e2a2c,#5d4a3e 55%,#3a2b24)" role="img" aria-label="Hotel reception desk with staff"></div><h3>Sed ut perspiciatis unde</h3><p>Lorem ipsum dolor sit amet, consect adipiscing elit. Praesent</p><div class="meta"><span class="stars">★★★<em>☆☆</em></span>From &nbsp;$102</div><div class="btn">Booking Now<span>»</span></div></article>
  <article class="abs card" style="left:212px"><div class="img" style="background:radial-gradient(ellipse 50px 18px at 40px 70px,rgba(245,235,220,.8),transparent),linear-gradient(180deg,#d8c3a0 0%,#6a4a34 45%,#3a2a20 100%)" role="img" aria-label="Hotel bedroom with warm lighting"></div><h3>Sed ut perspiciatis unde</h3><p>Lorem ipsum dolor sit amet, consect adipiscing elit. Praesent</p><div class="meta"><span class="stars">★★★<em>☆☆</em></span>From &nbsp;$102</div><div class="btn">Booking Now<span>»</span></div></article>
  <article class="abs card" style="left:365px"><div class="img" style="background:radial-gradient(ellipse 55px 22px at 70px 55px,#f1efe9,transparent),linear-gradient(180deg,#4f5e64 0%,#6f7b80 45%,#b8bcc2 75%,#8a8f96 100%)" role="img" aria-label="Hotel bedroom with white bed and lamps"></div><h3>Sed ut perspiciatis unde</h3><p>Lorem ipsum dolor sit amet, consect adipiscing elit. Praesent</p><div class="meta"><span class="stars">★★★<em>☆☆</em></span>From &nbsp;$102</div><div class="btn">Booking Now<span>»</span></div></article>
  <article class="abs card" style="left:518px"><div class="img" style="background:radial-gradient(ellipse 30px 50px at 120px 45px,#f5ece2,transparent),linear-gradient(160deg,#f0d3b3,#c99a74 55%,#8a5a3f)" role="img" aria-label="Hotel suite with dining table and shelves"></div><h3>Sed ut perspiciatis unde</h3><p>Lorem ipsum dolor sit amet, consect adipiscing elit. Praesent</p><div class="meta"><span class="stars">★★★<em>☆☆</em></span>From &nbsp;$102</div><div class="btn">Booking Now<span>»</span></div></article>
</section>

<section>
  <div class="abs person" role="img" aria-label="Smiling consultant in a suit with arms crossed"></div>
  <h2 class="abs c-title">CONTACT US TODAY</h2>
  <div class="abs c-lines">Name: Carla T. Whitmore<br>Email: CarlaTWhitmore@mailgrove.us<br>Phone: 555-301-4472</div>
  <div class="abs c-icon" style="left:217px;top:1004px"><svg width="14" height="13" viewBox="0 0 14 13"><path d="M7 1 L13 6.5 L11 6.5 L11 12 L8.5 12 L8.5 8.5 L5.5 8.5 L5.5 12 L3 12 L3 6.5 L1 6.5Z" fill="#222"/></svg></div>
  <div class="abs c-addr" style="top:1005px">NeonLodging.Offers, 18 West Harbor Ave.<br>Millbrook, PA 17330</div>
  <div class="abs c-icon" style="left:217px;top:1049px"><svg width="14" height="14" viewBox="0 0 14 14"><path d="M3 1 L5.5 1 L6.5 4 L5 5.3 C5.8 7 7 8.2 8.7 9 L10 7.5 L13 8.5 L13 11 C13 12 12 13 11 13 C5.5 12.5 1.5 8.5 1 3 C1 2 2 1 3 1Z" fill="#222"/></svg></div>
  <div class="abs c-addr" style="top:1050px">Phone No : &nbsp;+1 555 210 7734<br>Email: info@neonlodgingoffers.com</div>
  <span class="abs social" style="left:221px;background:#2a4f96"></span>
  <span class="abs social" style="left:242px;background:#2c9ad8"></span>
  <span class="abs social" style="left:263px;background:#333"></span>
  <span class="abs social" style="left:283px;background:#f06a1f"></span>
  <span class="abs social" style="left:304px;background:#d9251c"></span>

  <div class="abs enquiry"></div>
  <h3 class="abs e-title">NEED HELP?</h3>
  <div class="abs e-label" style="top:945px">Full Name</div>
  <div class="abs e-input" style="top:938px;height:23px"></div>
  <div class="abs e-label" style="top:977px">Phone No</div>
  <div class="abs e-input" style="top:970px;height:23px"></div>
  <div class="abs e-label" style="top:1007px">E Mail</div>
  <div class="abs e-input" style="top:1000px;height:23px"></div>
  <div class="abs e-label" style="top:1043px">Message</div>
  <div class="abs e-input" style="top:1036px;height:46px"></div>
  <div class="abs e-send">QUICK ENQUIRY</div>
</section>

<footer>
  <div class="abs footer"></div>
  <div class="abs f-links">HOME &nbsp;/ &nbsp;GROUPS &nbsp;/ &nbsp;SEARCH EVENTS &nbsp;/ &nbsp;NEONLODGING OFFERS &nbsp;/ &nbsp;CONTACT US</div>
  <div class="abs f-copy">COPYRIGHT © 2015 NEONLODGING.OFFERS. ALL RIGHTS RESERVED.</div>
</footer>
</body>
</html>
```